Redesign of Engineering firm website

I want a redesign of the torvelpower.com website with the below in mind:

1- the client has a 3 main sectors: Renewable Energy, Process Automation and General Engineering.
2- Home page should show the 3 sectors
3- the other standard pages should be home, About, Clients, Projects, Training, Career, and Contact
4- The theme should be wordpress.
5- Responsive layout that works with all devices
6- One page layout is preferable for the home page.
7- it should be original and is not copied from other templates.
Updates

Reason: As requested from so many designers... the deadline is extended. Thank you

Target Market(s)

Engineers and professional

Industry/Entity Type

Solar Energy

Font styles to use
Serif
Sans Serif

Colors
3277b5
0355a3
0493ce

Requirements
Must have
• pictures that represent the three sectors

```html
<!DOCTYPE html>
<html lang="en">
<head>
<meta charset="utf-8">
<title>Torvel Power – Home Design 1</title>
<link href="https://fonts.googleapis.com/css2?family=Montserrat:wght@300;400;500;600;700;800&family=Open+Sans:wght@400;600;700&display=swap" rel="stylesheet">
<style>
:root{
  --ink:#111;
  --muted:#6d6d6d;
  --label:#7b7b7b;
  --brand-blue:#0089b3;
  --login-blue:#0493ce;
  --accent-yellow:#ffcc00;
  --nav-yellow:#f5b800;
  --client-bg:#e1e1e1;
  --footer-bg:#3a3a3a;
  --footer-line:#4a4a4a;
  --white:#fff;
}
*{box-sizing:border-box;margin:0;padding:0}
html,body{width:1200px;height:1200px;overflow:hidden;background:#fff}
.board{width:1500px;height:1500px;transform:scale(.8);transform-origin:0 0;position:relative;font-family:"Open Sans",Arial,sans-serif}
.board-title{position:absolute;left:44px;top:76px;font-family:"Montserrat",sans-serif;font-weight:700;font-size:17px;color:var(--label);letter-spacing:.3px}

.site{position:absolute;left:662px;top:31px;width:742px;height:1438px;border:1px solid #bbb;overflow:hidden;background:#fff}
.abs{position:absolute}

/* hero */
.hero{left:0;top:0;width:742px;height:316px;background:linear-gradient(180deg,#241f22 0%,#3a2c2a 45%,#5a4033 70%,#3b3a44 82%,#5d5660 100%)}
.hero-panels{left:0;top:226px;width:742px;height:90px;background:linear-gradient(180deg,#3a3d4c,#6e6168)}
.logo{left:18px;top:18px;font-family:"Montserrat",sans-serif;font-weight:700;font-size:19px;color:var(--login-blue);letter-spacing:.5px}
.login{left:690px;top:12px;width:38px;height:16px;background:var(--login-blue);color:#fff;font-size:7px;display:flex;align-items:center;justify-content:center;gap:3px;font-weight:600}
.nav{right:13px;top:36px;display:flex;gap:14px;font-size:7px;font-weight:600;color:#fff}
.nav .active{color:var(--nav-yellow);border-left:1px solid var(--nav-yellow);border-right:1px solid var(--nav-yellow);padding:0 6px;margin-right:-6px}
.hero-copy{left:0;top:120px;width:742px;text-align:center;color:#fff;font-family:"Montserrat",sans-serif}
.hero-copy .lead{font-weight:400;font-size:22px;line-height:28px}
.hero-copy .strong{font-weight:700;font-size:22px;line-height:28px}
.hero-rule{width:280px;height:1px;background:#9c8a55;margin:10px auto 10px}
.hero-copy .sub{font-size:10.5px;font-weight:500;line-height:13px}

/* sector cards */
.sector-photo{width:214px;height:202px}
.sector-panel{width:297px;height:202px;padding:20px 22px 0 21px}
.sector-title{font-family:"Montserrat",sans-serif;font-weight:700;font-size:24px;line-height:30px;margin-bottom:9px}
.sector-body{font-size:8.3px;line-height:11.1px;width:245px}
.read-more{display:inline-block;margin-top:10px;font-size:8.3px;text-decoration:underline}
.renewable .sector-panel{background:var(--brand-blue);color:#fff}
.engineering .sector-panel{background:var(--accent-yellow);color:var(--ink)}
.photo-sky{background:linear-gradient(160deg,#1e6fc8 0%,#4a9be0 45%,#bcd9f2 75%,#4a8fd6 100%)}
.photo-workers{background:radial-gradient(circle at 55% 50%,#5a6a86 0%,#2f3a4e 45%,#9aa1ad 70%,#3d3f44 100%)}

/* process automation */
.process-title{left:116px;top:482px;font-family:"Montserrat",sans-serif;font-weight:700;font-size:27px;line-height:30px;color:var(--ink)}
.process-body{left:116px;top:554px;width:162px;font-size:8.3px;line-height:11.1px;color:var(--muted)}
.process-body p+p{margin-top:11px}
.process-body .read-more{color:#333}
.gear-photo{left:340px;top:462px;width:300px;height:250px;background:radial-gradient(circle at 55% 55%,#9a9a9a 0%,#d6d6d6 35%,#f4f4f4 60%,#fff 75%)}

/* clients */
.clients{left:0;top:939px;width:742px;height:157px;background:var(--client-bg)}
.clients-label{top:22px;width:742px;text-align:center;font-family:"Montserrat",sans-serif;font-weight:500;font-size:8.5px;color:#333}
.client-box{top:52px;width:101px;height:67px;border:1px solid #b9b9b9;background:#e4e4e4;display:flex;align-items:center;justify-content:center;font-family:"Open Sans",sans-serif;font-weight:600;font-size:11px;color:#555}
.arrow{top:79px;width:14px;height:14px;border-radius:50%;background:#c9c9c9}

/* testimonial */
.quote-mark{width:742px;text-align:center;color:var(--brand-blue);font-family:"Montserrat",sans-serif;font-weight:800}
.quote-text{left:0;top:1149px;width:742px;text-align:center;font-family:"Montserrat",sans-serif;font-size:11.5px;line-height:14px;color:var(--ink)}
.quote-author{left:0;top:1209px;width:742px;text-align:center;color:#9a9a9a;font-family:"Montserrat",sans-serif}
.quote-author .name{font-size:8px}
.quote-author .role{font-size:5.5px;line-height:7px}

/* footer */
.footer{left:0;top:1252px;width:742px;height:186px;background:var(--footer-bg);color:#fff}
.footer-head{font-family:"Montserrat",sans-serif;font-weight:700;font-size:7.5px;color:var(--nav-yellow)}
.footer-list{list-style:none;font-family:"Montserrat",sans-serif;font-weight:600;font-size:5.5px;line-height:11px}
.tweet{width:130px;font-size:5.5px;line-height:9px;color:#8d8d8d}
.tweet b{color:#fff}
.contact{font-family:"Montserrat",sans-serif;font-size:5.5px;line-height:8.5px;font-weight:600}
.footer-rule{left:0;top:128px;width:742px;height:1px;background:var(--footer-line)}
.copyright{left:0;top:141px;width:742px;text-align:center;font-size:5.5px;color:#bbb}
.social{left:327px;top:160px;display:flex;gap:3px}
.social span{width:12px;height:12px;border-radius:50%;background:#8a8a8a}
</style>
</head>
<body>
<div class="board">
  <div class="board-title">HOME DESIGN 1</div>

  <div class="site">
    <!-- hero -->
    <div class="abs hero" role="img" aria-label="Wind turbines at dusk above a field of solar panels"></div>
    <div class="abs hero-panels" role="img" aria-label="Rows of solar panels"></div>
    <div class="abs logo">TORVEL</div>
    <div class="abs login">
      <svg width="6" height="6" viewBox="0 0 10 10"><circle cx="5" cy="3" r="2.4" fill="#fff"/><path d="M0.5 10c0-3 2-4.5 4.5-4.5S9.5 7 9.5 10z" fill="#fff"/></svg>Login
    </div>
    <nav class="abs nav">
      <span class="active">Home</span><span>About Us</span><span>Services</span><span>Training</span><span>Employment</span><span>Contact Us</span>
    </nav>
    <div class="abs hero-copy">
      <div class="lead">We are the experts of</div>
      <div class="strong">Solar Power Technology.</div>
      <div class="hero-rule"></div>
      <div class="sub">We help providers of solar and clean energy solutions reach new customers<br>and grow their business profitably.</div>
    </div>

    <!-- renewable energy -->
    <div class="abs renewable" style="left:116px;top:242px;display:flex">
      <div class="sector-photo photo-sky" role="img" aria-label="Wind turbines against a bright blue sky"></div>
      <div class="sector-panel">
        <h2 class="sector-title">Renewable Energy</h2>
        <p class="sector-body">Lorem ipsum dolor sit amet, consectetur adipiscing elit. Vivamus eget elit ut ex ultricies aliquam. Nullam varius quis massa et sollicitudin. Curabitur eget justo quis nisl convallis vestibulum in et felis. Proin ullamcorper, dolor non luctus dapibus, magna lorem pretium turpis, id convallis nulla nunc in nibh. Vestibulum ante ipsum primis in faucibus orci luctus et ultrices posuere cubilia Curae; Aenean sit amet tellus nisi. Proin tristique sem faucibus posuere pretium.</p>
        <span class="read-more">Read More</span>
      </div>
    </div>

    <!-- process automation -->
    <h2 class="abs process-title">Process<br>Automation</h2>
    <div class="abs process-body">
      <p>Mauris maximus diam nec viverra fringilla. Aenean vehicula iaculis metus. Aenean quis laoreet enim, id dapibus metus. Integer porttitor nulla vitae lectus consectetur, nec efficitur lacus congue.</p>
      <p>Donec rhoncus turpis ut semper mattis. Nunc nec vehicula metus. Lorem ipsum dolor sit amet, consectetur adipiscing elit.</p>
      <span class="read-more">Read More</span>
    </div>
    <div class="abs gear-photo" role="img" aria-label="Interlocking steel gears inside a large white cog"></div>

    <!-- general engineering -->
    <div class="abs engineering" style="left:116px;top:717px;display:flex">
      <div class="sector-photo photo-workers" role="img" aria-label="Two engineers in hard hats framed by a large gear"></div>
      <div class="sector-panel">
        <h2 class="sector-title">General Engineering</h2>
        <p class="sector-body">Lorem ipsum dolor sit amet, consectetur adipiscing elit. Vivamus eget elit ut ex ultricies aliquam. Nullam varius quis massa et sollicitudin. Curabitur eget justo quis nisl convallis vestibulum in et felis. Proin ullamcorper, dolor non luctus dapibus, magna lorem pretium turpis, id convallis nulla nunc in nibh. Vestibulum ante ipsum primis in faucibus orci luctus et ultrices posuere cubilia Curae; Aenean sit amet tellus nisi. Proin tristique sem faucibus posuere pretium.</p>
        <span class="read-more">Read More</span>
      </div>
    </div>

    <!-- clients -->
    <section class="abs clients">
      <div class="abs clients-label">OUR CLIENT</div>
      <div class="abs arrow" style="left:125px"><svg width="14" height="14" viewBox="0 0 14 14"><path d="M8 4 5 7l3 3" stroke="#fff" stroke-width="1.6" fill="none"/></svg></div>
      <div class="abs client-box" style="left:154px">Calvia Bank</div>
      <div class="abs client-box" style="left:264px">Harlow Trust</div>
      <div class="abs client-box" style="left:374px">Corvane</div>
      <div class="abs client-box" style="left:484px">Haneul Motors</div>
      <div class="abs arrow" style="left:603px"><svg width="14" height="14" viewBox="0 0 14 14"><path d="M6 4l3 3-3 3" stroke="#fff" stroke-width="1.6" fill="none"/></svg></div>
    </section>

    <!-- testimonial -->
    <div class="abs quote-mark" style="left:0;top:1103px;font-size:44px;line-height:44px">&ldquo;</div>
    <p class="abs quote-text">Brookvale was able to grow over 100% during the<br>recession when other dentists were experiencing<br>an overall decline.</p>
    <div class="abs quote-mark" style="left:0;top:1188px;font-size:26px;line-height:26px">&rdquo;</div>
    <div class="abs quote-author">
      <div class="name">Mara L. Denholm, Esquire</div>
      <div class="role">Attorney at Law for<br>BROOKVALE DENTAL CENTER, INC.</div>
    </div>

    <!-- footer -->
    <footer class="abs footer">
      <div class="abs footer-head" style="left:135px;top:15px">MENU</div>
      <ul class="abs footer-list" style="left:135px;top:28px">
        <li>HOME</li><li>ABOUT US</li><li>SERVICES</li><li>TRAINING</li><li>EMPLOYMENT</li><li>CONTACT US</li>
      </ul>
      <ul class="abs footer-list" style="left:238px;top:28px">
        <li>CLIENTS</li><li>PRIVACY POLICY</li><li>SUPPORT</li>
      </ul>
      <div class="abs footer-head" style="left:335px;top:15px">LATEST TWEETS</div>
      <p class="abs tweet" style="left:336px;top:30px">There's still no update, my server is down over 3 days and I am losing thousands of dollars. <b>https://tvl.co/x4Rk29pa</b><br><b>01:11 AM Jan 09th</b></p>
      <p class="abs tweet" style="left:336px;top:75px">There's still no update, my server is down over 3 days and I am losing thousands of dollars. <b>https://tvl.co/x4Rk29pa</b><br><b>01:11 AM Jan 09th</b></p>
      <div class="abs footer-head" style="left:515px;top:15px">GET IN TOUCH</div>
      <div class="abs contact" style="left:515px;top:30px;font-size:6px;font-weight:700">TORVEL POWER CONSULTING</div>
      <div class="abs contact" style="left:515px;top:45px">Qaryat Bay&nbsp; Eastern<br>Province 48210<br>Kingdom of Saudi Arabia</div>
      <div class="abs contact" style="left:515px;top:78px">T&nbsp; +966130000457</div>
      <div class="abs contact" style="left:515px;top:91px;font-weight:400">info@torvelpower.com</div>
      <div class="abs footer-rule"></div>
      <div class="abs copyright">Copyright © 2017 TORVEL POWER CONSULTING. All rights reserved.</div>
      <div class="abs social"><span></span><span></span><span></span><span></span><span></span><span></span></div>
    </footer>
  </div>
</div>
</body>
</html>
```